Flyer-Design für Immobilienfirma
Zielgruppe
www.brenkholt-immobilien.de
Aufgabenstellung
Thema :
Neukunden generieren – Viele Wege führen zu neuen Leads ...
Sich selbst als Experten platzieren mit Bild
Dienstleistung : FÜR DEN IMMOBILIENBESITZER
Was ist Ihre Immobilie wert?
KOSTENLOSE Beratung durch Experten
KOSTENLOSE Immobilienbewertung
KOSTENLOS vorhandene Grundrisszeichnungen aktualisieren
KOSTENLOS 3D Grundrisszeichnungen und Ansicht
KOSTENLOS 3D Fotos und 360 Grad Ansichten
KOSTENLOS Drohnenaufnahmen IHRER Immobilien
KOSTENLOS Erstellung eines Energieverbrauchsausweises
evtl für die Rückseite
#Tippgeberprämie
Brenkholt & Partner Immobilien
so einfach verdienen Sie sich Ihre Tippprämie
wenn Sie Kenntnis vom beabsichtigten Verkauf einer Immobilie haben, dann setzen Sie sich mit uns in Verbindung.
Wir belohnen Ihren Tipp – wenn er zu einem Verkaufsabschluss durch uns führt –
mit 10 Prozent der an uns gezahlten Netto-Vermittlungsprovision (ohne MwSt.).
Dies gilt auch für Eigentümer, die uns Ihre Immobilie zum Verkauf geben.
Voraussetzungen für die Zahlung einer Tippgeber-Prämie sind:
Die Brenkholt & Partner immobilien kennt das angebotene Objekt noch nicht.
Das Objekt wird nicht bereits im Internet von dritter Seite beworben.
Die Brenkholt & Partner immobilien erhält die Erlaubnis zur Vermarktung der Immobilie.
Es kommt zu einem durch die Brenkholt & Partner immobilien vermittelten Verkauf
Sie erhalten Ihre Tippprämie unmittelbar nach Zahlung der Courtage an uns auf ein von Ihnen genanntes Konto überwiesen!

```html
<!DOCTYPE html>
<html lang="de">
<head>
<meta charset="utf-8">
<title>Tippgeberprämie – Brenkholt & Partner</title>
<link href="https://fonts.googleapis.com/css2?family=Josefin+Sans:wght@300;400;600;700&display=swap" rel="stylesheet">
<style>
  :root {
    --gold: #dbb057;
    --panel: #ececec;
    --ink: #2a2a2a;
    --muted: #6d6d6d;
    --title: #666666;
    --brand: #4a3b2c;
    --page-bg: #e4e4e4;
    --paper: #ffffff;
  }
  html, body {
    margin: 0;
    width: 1200px;
    height: 1200px;
    overflow: hidden;
    background: var(--page-bg);
    font-family: "Josefin Sans", sans-serif;
  }
  .flyer {
    position: absolute;
    left: 191px;
    top: 20px;
    width: 818px;
    height: 1160px;
    background: var(--paper);
  }
  .brand {
    position: absolute;
    left: 571px;
    top: 84px;
    color: var(--brand);
  }
  .brand-name {
    font-size: 28px;
    font-weight: 600;
    line-height: 1;
  }
  .brand-sub {
    font-size: 11px;
    font-weight: 400;
    margin-left: 60px;
    margin-top: 4px;
  }
  .title {
    position: absolute;
    left: 25px;
    top: 192px;
    margin: 0;
    font-size: 35px;
    font-weight: 300;
    color: var(--title);
    letter-spacing: 0.5px;
  }
  .intro {
    position: absolute;
    left: -3px;
    top: 263px;
    width: 370px;
    height: 195px;
    background: var(--panel);
  }
  .accent-bar {
    position: absolute;
    left: -3px;
    width: 26px;
    background: var(--gold);
  }
  .accent-bar.top { top: 263px; height: 195px; }
  .accent-bar.mid { top: 476px; height: 194px; }
  .accent-bar.low { top: 688px; height: 194px; }
  .intro p {
    position: absolute;
    left: 41px;
    top: 10px;
    width: 320px;
    margin: 0;
    font-size: 20.5px;
    line-height: 33.3px;
    color: var(--ink);
  }
  .photo {
    position: absolute;
    left: 384px;
    top: 263px;
    width: 436px;
    height: 195px;
    background: linear-gradient(90deg, #e9e9e9 0%, #b9b4ae 40%, #8f8078 60%, #e8d7cb 85%, #f1e6dd 100%);
  }
  .badge {
    position: absolute;
    left: 155px;
    top: 430px;
    width: 200px;
    height: 200px;
    overflow: visible;
  }
  .copy {
    position: absolute;
    left: 386px;
    top: 490px;
    width: 397px;
    color: var(--muted);
    font-size: 17.5px;
    font-weight: 300;
    line-height: 27.4px;
  }
  .copy p { margin: 0; }
  .copy strong { font-weight: 600; color: #555; }
  .copy .lead { margin-bottom: 11px; }
  .conditions-head {
    padding-bottom: 4px;
    border-bottom: 1px solid var(--gold);
  }
  .conditions {
    list-style: none;
    margin: 0 0 13px;
    padding: 0;
  }
  .conditions li {
    padding: 3px 0 2px 11px;
    text-indent: -11px;
    border-bottom: 1px solid var(--gold);
  }
  .conditions li::before { content: "· "; }
  .call {
    position: absolute;
    left: 47px;
    top: 979px;
    margin: 0;
    font-size: 24.5px;
    font-weight: 300;
    line-height: 27px;
    color: var(--ink);
  }
  .footer {
    position: absolute;
    left: 25px;
    top: 1078px;
    width: 795px;
    height: 83px;
    background: var(--gold);
    color: #fff;
    font-size: 17px;
    font-weight: 300;
    display: flex;
    align-items: center;
    justify-content: center;
    gap: 10px;
  }
</style>
</head>
<body>
  <main class="flyer">
    <div class="brand">
      <div class="brand-name">Brenkholt</div>
      <div class="brand-sub">&amp; Partner Real Estate</div>
    </div>

    <h1 class="title">TIPPGEBERPRÄMIE</h1>

    <div class="intro">
      <p>So einfach verdienen Sie sich Ihre Tippprämie wenn Sie Kenntnis vom beabsichtigten Verkauf einer Immobilie haben, dann setzen Sie sich mit uns in Verbindung.</p>
    </div>
    <div class="accent-bar top"></div>
    <div class="accent-bar mid"></div>
    <div class="accent-bar low"></div>

    <div class="photo" role="img" aria-label="Foto: Frau flüstert einem Mann einen Tipp ins Ohr"></div>

    <svg class="badge" viewBox="0 0 200 200" aria-label="Tippgeberprämie 10%">
      <polygon fill="var(--gold)" transform="rotate(-8 100 100)"
        points="100,2 129.9,27.9 169.3,30.7 172.1,70.1 198,100 172.1,129.9 169.3,169.3 129.9,172.1 100,198 70.1,172.1 30.7,169.3 27.9,129.9 2,100 27.9,70.1 30.7,30.7 70.1,27.9"/>
      <g transform="rotate(-10 100 100)" fill="#fff" font-family="Josefin Sans, sans-serif" font-weight="700" font-size="28" text-anchor="middle">
        <text x="92" y="64">TIPP</text>
        <text x="98" y="98">GEBER-</text>
        <text x="104" y="132">PRÄMIE</text>
        <text x="112" y="164">10%</text>
      </g>
    </svg>

    <section class="copy">
      <p class="lead"><strong>Wir belohnen Ihren Tipp</strong> – wenn er zu einem Ver&shy;kaufsabschluss durch uns führt – mit 10 Prozent der an uns gezahlten Netto-Vermittlungsprovision (ohne MwSt.). Dies gilt auch für Eigentümer, die uns Ihre Immobilie zum Verkauf geben.</p>
      <p class="conditions-head"><strong>Voraussetzungen für die Zahlung einer Tipp&shy;geber-Prämie sind:</strong></p>
      <ul class="conditions">
        <li>Die Brenkholt &amp; Partner immobilien kennt das angebotene Objekt noch nicht.</li>
        <li>Das Objekt wird nicht bereits im Internet von dritter Seite beworben.</li>
        <li>Die Brenkholt &amp; Partner immobilien erhält die Erlaubnis zur Vermarktung der Immobilie.</li>
        <li>Es kommt zu einem durch die Brenkholt &amp; Partner immobilien vermittelten Verkauf</li>
      </ul>
      <p>Sie erhalten Ihre Tippprämie unmittelbar nach Zah&shy;lung der Courtage an uns auf ein von Ihnen genann&shy;tes Konto überwiesen!</p>
    </section>

    <p class="call">Rufen Sie uns an?<br>+49 (0) 421 55 31 20 48-10</p>

    <footer class="footer">
      <span>www.brenkholt-immobilien.de</span><span>|</span><span>contact@brenkholt-immobilien.de</span>
    </footer>
  </main>
</body>
</html>
```